Redesign of iOS App Moriva Tutor

Redesign of existing App Moriva Tutor, an app that helps learning Japanese Kanjis, Hiragana, Katakana.

The functionallity should remain the same as today: the app is free, you may download it at the app store. But: I like the design of my other apps better ;)

Target Market(s)

Students learning Japanese

Industry/Entity Type

Teacher

Font styles to use
Sans Serif

Requirements
Must have
• Moriva Tutor has 7 main screens, all screens has to be designed for iPhone and iPad: Main, Settings, Reading Tests, Writing Tests, Game, Paper Mode, Search
Nice to have
• I like the logo as it is today

```html
<!DOCTYPE html>
<html lang="en">
<head>
<meta charset="utf-8">
<title>Moriva Tutor – UI Design Concept</title>
<link rel="stylesheet" href="https://fonts.googleapis.com/css2?family=Roboto:wght@300;400;500;700&family=Noto+Sans+JP:wght@300;400;500;700&display=swap">
<style>
  :root{
    --red:#be1b2f;
    --red-dark:#9a1222;
    --red-soft:#e05a6a;
    --coral:#f25a4a;
    --teal:#17c2a4;
    --blue:#3c93e6;
    --grey:#9e9e9e;
    --pink-cell:#f3dadd;
    --light:#f3f3f3;
    --line:#e3e3e3;
    --ink:#222;
    --muted:#8a8a8a;
    --link:#3c93e6;
    --orange:#f7a95c;
    --white:#fff;
  }
  *{box-sizing:border-box;margin:0;padding:0}
  html,body{width:1200px;height:1200px;overflow:hidden}
  body{font-family:"Roboto","Noto Sans JP",sans-serif;color:var(--ink)}
  .canvas{width:1200px;height:1200px;overflow:hidden;position:relative}
  .stage{position:absolute;left:0;top:0;width:1500px;height:1500px;transform:scale(.8);transform-origin:0 0;
    background:linear-gradient(180deg,var(--red) 0%,var(--red) 60%,#e4713f 80%,var(--orange) 100%)}
  .abs{position:absolute}
  .c{transform:translateX(-50%);text-align:center;white-space:nowrap}
  .jp{font-family:"Noto Sans JP",sans-serif}
  .screen-title{position:absolute;width:307px;text-align:center;color:var(--white);font-weight:500;font-size:17px}
  .screen{position:absolute;width:307px;height:542px;background:var(--white);overflow:hidden}
  .status{position:absolute;left:0;top:0;width:100%;height:16px;font-size:9px;font-weight:500}
  .status .dots{left:6px;top:3px;letter-spacing:-1px}
  .status .time{left:153px;top:3px}
  .status .batt{right:8px;top:3px;display:flex;align-items:center;gap:3px}
  .status .batt i{display:inline-block;width:18px;height:7px;background:#222;border-radius:1px}
  .nav-label{font-size:12px;font-weight:500}
  .counter .k{font-size:12px;font-weight:500;letter-spacing:.2px}
  .counter .v{font-size:14px;margin-top:3px}
  .card{position:absolute;background:var(--white);box-shadow:0 2px 8px rgba(0,0,0,.15)}
  .legend{font-size:9px;display:flex;gap:4px;align-items:center}
  .dot{display:inline-block;width:8px;height:8px;border-radius:50%}
  .pair-grid{position:absolute;left:29px;top:65px;width:248px;display:grid;grid-template-columns:122px 122px;gap:4px}
  .pair{background:var(--pink-cell);height:71px;position:relative}
  .pair .lbl{position:absolute;left:0;right:0;top:9px;text-align:center;font-size:9.5px}
  .pill{position:absolute;width:47px;height:12px;border-radius:6px;color:var(--white);font-size:8.5px;text-align:center;line-height:12px}
  .pill.g{background:var(--grey)} .pill.t{background:var(--teal)} .pill.b{background:var(--blue)} .pill.r{background:var(--coral)}
  .tabs{position:absolute;left:18px;top:455px;width:270px;height:35px;display:flex;font-size:12px;font-weight:500;border-top:1px solid var(--line)}
  .tabs span{flex:1;text-align:center;line-height:35px}
  .tabs .on{background:var(--red);color:var(--white)}
  .word-grid{position:absolute;left:18px;top:171px;width:270px;height:270px;display:grid;grid-template-columns:repeat(3,90px);grid-template-rows:repeat(3,90px);background:var(--light)}
  .word-grid span{display:flex;align-items:center;justify-content:center;font-size:9.5px}
  .word-grid .hit{background:var(--coral);color:var(--white)}
  .word-grid .ok{background:var(--teal);color:var(--white)}
  .tally{font-size:9.5px;display:flex;align-items:center;gap:5px}
  .pop-row{position:absolute;font-size:9px;white-space:nowrap}
  .pop-head{position:absolute;left:28px;width:255px;display:flex;align-items:center;gap:6px;font-size:8.5px;color:var(--muted)}
  .pop-head::before,.pop-head::after{content:"";flex:1;height:1px;background:var(--line)}
  .en{color:var(--link)}
  .kanji-grid{position:absolute;left:18px;top:170px;width:270px;height:270px;display:grid;grid-template-columns:repeat(3,90px);grid-template-rows:repeat(3,90px);background:#f7f7f7}
  .kanji-grid span{display:flex;align-items:center;justify-content:center;font-size:19px;font-family:"Noto Sans JP",sans-serif}
  .kanji-grid .dim{color:#c4c4c4}
  .power{position:absolute;width:34px;height:34px;border-radius:50%;color:var(--white);font-size:6px;font-weight:700;text-align:center;display:flex;align-items:center;justify-content:center;line-height:1.1;box-shadow:0 2px 4px rgba(0,0,0,.25)}
  .stack{position:absolute;background:#e6e6e6;border-radius:3px}
  .band{position:absolute;left:18px;width:270px;background:var(--red);color:var(--white);text-align:center}
  .next{position:absolute;left:18px;width:270px;height:38px;background:var(--red-dark);color:var(--white);font-size:12px;font-weight:500;text-align:center;line-height:38px}
  .kana{position:absolute;left:18px;font-size:24px;font-family:"Noto Sans JP",sans-serif;line-height:1}
  .srow{position:absolute;left:70px;width:230px;font-size:9px;height:14px}
  .mini{display:inline-block;width:9px;height:9px;border-radius:50%;background:#9a9a9a;margin-right:3px}
  .star{position:absolute;font-size:16px;line-height:1}
  .set-label{position:absolute;left:18px;font-size:9.5px}
  .seg{position:absolute;left:18px;width:270px;height:30px;border-radius:15px;background:var(--light);display:flex;font-size:9.5px}
  .seg span{flex:1;text-align:center;line-height:30px;border-radius:15px}
  .seg .on{background:var(--red);color:var(--white)}
  .app-mark{position:absolute;left:72px;top:1277px;width:120px;height:120px;border-radius:26px;background:var(--red)}
  .brand{position:absolute;left:221px;top:1272px;color:var(--white);font-size:30px;font-weight:700}
  .tagline{position:absolute;left:221px;top:1313px;color:var(--white);font-size:18px;font-weight:500}
  .about{position:absolute;left:221px;top:1351px;width:1230px;color:var(--white);font-size:20px;line-height:24px}
</style>
</head>
<body>
<div class="canvas">
<div class="stage">

  <!-- ================= HOME ================= -->
  <div class="screen-title" style="left:72px;top:47px">Home</div>
  <div class="screen" style="left:72px;top:78px">
    <div class="status"><span class="abs dots">●●●●● ᯤ</span><span class="abs time c">9:41 AM</span><span class="abs batt">100% <i></i></span></div>
    <div class="card" style="left:18px;top:37px;width:270px;height:416px"></div>
    <div class="abs legend" style="left:28px;top:47px"><i class="dot" style="background:var(--grey)"></i>Test</div>
    <div class="abs legend" style="left:94px;top:47px"><i class="dot" style="background:var(--teal)"></i>Correct</div>
    <div class="abs legend" style="left:166px;top:47px"><i class="dot" style="background:var(--blue)"></i>Score</div>
    <div class="abs legend" style="left:234px;top:47px"><i class="dot" style="background:var(--coral)"></i>Wrong</div>
    <div class="pair-grid">
      <div class="pair"><div class="lbl">Kanji → Meaning</div><span class="pill g" style="left:9px;top:27px">103</span><span class="pill t" style="left:66px;top:27px">0</span><span class="pill b" style="left:9px;top:49px">0</span><span class="pill r" style="left:66px;top:49px">0</span></div>
      <div class="pair"><div class="lbl">Meaning → Kanji</div><span class="pill g" style="left:9px;top:27px">103</span><span class="pill t" style="left:66px;top:27px">0</span><span class="pill b" style="left:9px;top:49px">0</span><span class="pill r" style="left:66px;top:49px">0</span></div>
      <div class="pair"><div class="lbl">Kanji → On</div><span class="pill g" style="left:9px;top:27px">103</span><span class="pill t" style="left:66px;top:27px">0</span><span class="pill b" style="left:9px;top:49px">0</span><span class="pill r" style="left:66px;top:49px">0</span></div>
      <div class="pair"><div class="lbl">On → Kanji</div><span class="pill g" style="left:9px;top:27px">103</span><span class="pill t" style="left:66px;top:27px">0</span><span class="pill b" style="left:9px;top:49px">0</span><span class="pill r" style="left:66px;top:49px">0</span></div>
      <div class="pair"><div class="lbl">Kanji → Kun</div><span class="pill g" style="left:9px;top:27px">103</span><span class="pill t" style="left:66px;top:27px">0</span><span class="pill b" style="left:9px;top:49px">0</span><span class="pill r" style="left:66px;top:49px">0</span></div>
      <div class="pair"><div class="lbl">Kun → Kanji</div><span class="pill g" style="left:9px;top:27px">103</span><span class="pill t" style="left:66px;top:27px">0</span><span class="pill b" style="left:9px;top:49px">0</span><span class="pill r" style="left:66px;top:49px">0</span></div>
      <div class="pair"><div class="lbl">Word → Reading</div><span class="pill g" style="left:9px;top:27px">103</span><span class="pill t" style="left:66px;top:27px">0</span><span class="pill b" style="left:9px;top:49px">0</span><span class="pill r" style="left:66px;top:49px">0</span></div>
      <div class="pair"><div class="lbl">Reading → Word</div><span class="pill g" style="left:9px;top:27px">103</span><span class="pill t" style="left:66px;top:27px">0</span><span class="pill b" style="left:9px;top:49px">0</span><span class="pill r" style="left:66px;top:49px">0</span></div>
      <div class="pair"><div class="lbl">Writing</div><span class="pill g" style="left:9px;top:27px">103</span><span class="pill t" style="left:66px;top:27px">0</span><span class="pill b" style="left:9px;top:49px">0</span><span class="pill r" style="left:66px;top:49px">0</span></div>
      <div class="pair"><div class="lbl">All Tests</div><span class="pill g" style="left:9px;top:27px">103</span><span class="pill t" style="left:66px;top:27px">0</span><span class="pill b" style="left:9px;top:49px">0</span><span class="pill r" style="left:66px;top:49px">0</span></div>
    </div>
    <div class="tabs"><span>K</span><span class="on">N5</span><span>N4</span><span>N3</span><span>N2</span><span>N1</span><span>★</span></div>
    <div class="abs nav-label c" style="left:52px;top:510px">Game</div>
    <div class="abs nav-label c" style="left:119px;top:510px">Paper</div>
    <div class="abs nav-label c" style="left:187px;top:510px">Search</div>
    <div class="abs nav-label c" style="left:254px;top:510px">Setting</div>
  </div>

  <!-- ================= TEST ================= -->
  <div class="screen-title" style="left:422px;top:47px">Test</div>
  <div class="screen" style="left:422px;top:78px">
    <div class="status"><span class="abs dots">●●●●● ᯤ</span><span class="abs time c">9:41 AM</span><span class="abs batt">100% <i></i></span></div>
    <div class="abs counter c" style="left:63px;top:42px"><div class="k">REMAINING</div><div class="v">102</div></div>
    <div class="abs counter c" style="left:154px;top:42px"><div class="k">WRONG</div><div class="v">1</div></div>
    <div class="abs counter c" style="left:243px;top:42px"><div class="k">CORRECT</div><div class="v">0</div></div>
    <div class="card" style="left:18px;top:88px;width:270px;height:352px"></div>
    <div class="abs c jp" style="left:153px;top:100px;font-size:30px">名</div>
    <div class="abs c jp" style="left:153px;top:140px;font-size:10px;color:var(--muted)">メイ、ミョウ、な</div>
    <div class="abs star" style="left:263px;top:97px">☆</div>
    <div class="word-grid">
      <span>seven</span><span class="hit">person</span><span>long</span>
      <span class="ok">name</span><span>come</span><span>many</span>
      <span>write</span><span>in</span><span>station</span>
    </div>
    <div class="abs tally" style="left:54px;top:464px"><i class="dot" style="background:var(--teal)"></i>Correct</div>
    <div class="abs c jp" style="left:153px;top:453px;width:36px;height:36px;border-radius:50%;background:var(--white);box-shadow:0 1px 5px rgba(0,0,0,.2);line-height:36px;font-size:13px">名</div>
    <div class="abs tally" style="left:208px;top:464px"><i class="dot" style="background:var(--coral)"></i>Wrong</div>
    <div class="abs nav-label c" style="left:153px;top:510px">Home</div>
  </div>

  <!-- ================= POPUP ================= -->
  <div class="screen-title" style="left:773px;top:47px">Popup</div>
  <div class="screen" style="left:773px;top:78px">
    <div class="status"><span class="abs dots">●●●●● ᯤ</span><span class="abs time c">9:41 AM</span><span class="abs batt">100% <i></i></span></div>
    <div class="card" style="left:18px;top:27px;width:270px;height:426px"></div>
    <div class="abs c jp" style="left:153px;top:33px;font-size:44px;font-weight:300"><span style="color:#bdbdbd">外国</span>語</div>
    <div class="abs c jp" style="left:153px;top:91px;font-size:9px;color:var(--muted)">がいこくご</div>
    <div class="abs c" style="left:153px;top:104px;font-size:9.5px">foreign language</div>
    <div class="abs" style="left:18px;top:122px;width:270px;height:1px;background:var(--line)"></div>
    <div class="pop-row jp" style="left:27px;top:130px">語 &nbsp;word</div>
    <div class="pop-row jp" style="left:118px;top:130px">ゴ</div>
    <div class="pop-row jp" style="left:118px;top:143px">かた<span class="en">る</span>, かた<span class="en">らう</span></div>
    <div class="pop-row" style="left:263px;top:130px">N5</div>
    <div class="pop-head jp" style="top:168px">Non-trivial Components of Kanji 語</div>
    <div class="pop-row jp" style="left:27px;top:183px">言 &nbsp;say</div><div class="pop-row jp" style="left:118px;top:183px">ゲン, ゴン</div><div class="pop-row jp" style="left:190px;top:183px">い-, こと</div><div class="pop-row" style="left:263px;top:183px">N5</div>
    <div class="pop-row jp" style="left:27px;top:197px">五 &nbsp;five</div><div class="pop-row jp" style="left:118px;top:197px">ゴ</div><div class="pop-row jp" style="left:190px;top:197px">いつ-</div><div class="pop-row" style="left:263px;top:197px">N5</div>
    <div class="pop-head" style="top:220px">Similar Pronunciation and in Group N5</div>
    <div class="pop-row jp" style="left:27px;top:235px">五 &nbsp;five</div><div class="pop-row jp" style="left:118px;top:235px">ゴ</div><div class="pop-row jp" style="left:190px;top:235px">いつ-</div><div class="pop-row" style="left:263px;top:235px">N5</div>
    <div class="pop-row jp" style="left:27px;top:250px">午 &nbsp;noon</div><div class="pop-row jp" style="left:118px;top:250px">ゴ</div><div class="pop-row" style="left:263px;top:250px">N5</div>
    <div class="pop-row jp" style="left:27px;top:265px">後 &nbsp;behind</div><div class="pop-row jp" style="left:118px;top:265px">ゴ, コウ</div><div class="pop-row jp" style="left:190px;top:265px">あと, うし-,…</div><div class="pop-row" style="left:263px;top:265px">N5</div>
    <div class="pop-head jp" style="top:287px">Example Words for 語 used in Tests</div>
    <div class="pop-row jp" style="left:27px;top:302px">言語<br><span class="en">language</span></div><div class="pop-row jp" style="left:118px;top:302px">げんご</div>
    <div class="pop-row jp" style="left:27px;top:332px">用語<br><span class="en">term, terminology</span></div><div class="pop-row jp" style="left:118px;top:332px">ようご</div>
    <div class="pop-row jp" style="left:27px;top:362px">外国語<br><span class="en">foreign language</span></div><div class="pop-row jp" style="left:118px;top:362px">がいこくご</div>
    <div class="pop-row jp" style="left:27px;top:392px">国語<br><span class="en">national language</span></div><div class="pop-row jp" style="left:118px;top:392px">こくご</div>
    <div class="pop-row jp" style="left:27px;top:422px">語る<br><span class="en">to talk about, to speak of, to tell, to narrate</span></div><div class="pop-row jp" style="left:118px;top:422px">かたる</div>
    <div class="abs tally" style="left:54px;top:464px"><i class="dot" style="background:var(--teal)"></i>Correct</div>
    <div class="abs c" style="left:153px;top:452px;width:36px;height:36px;border-radius:50%;background:var(--red);color:var(--white);line-height:36px;font-size:20px;font-weight:300">✕</div>
    <div class="abs tally" style="left:208px;top:464px"><i class="dot" style="background:var(--coral)"></i>Wrong</div>
    <div class="abs nav-label c" style="left:153px;top:510px">Home</div>
  </div>

  <!-- ================= GAME ================= -->
  <div class="screen-title" style="left:1121px;top:47px">Game</div>
  <div class="screen" style="left:1121px;top:78px">
    <div class="status"><span class="abs dots">●●●●● ᯤ</span><span class="abs time c">9:41 AM</span><span class="abs batt">100% <i></i></span></div>
    <div class="abs counter c" style="left:63px;top:31px"><div class="k">Lives</div><div class="v">3</div><div style="font-size:6.5px;margin-top:2px">Level N5</div></div>
    <div class="abs counter c" style="left:153px;top:31px"><div class="k">Score</div><div class="v">0</div><div style="font-size:6.5px;margin-top:2px">Highscore : 8</div></div>
    <div class="abs counter c" style="left:243px;top:31px"><div class="k">Coins</div><div class="v">12</div></div>
    <div class="card" style="left:18px;top:88px;width:270px;height:352px"></div>
    <div class="abs c jp" style="left:153px;top:110px;font-size:30px">ハク, ビャク</div>
    <div class="kanji-grid">
      <span class="dim">国</span><span class="dim">石</span><span>年</span>
      <span>七</span><span class="dim">外</span><span class="dim">毎</span>
      <span>一</span><span>白</span><span class="dim">新</span>
    </div>
    <div class="power" style="left:42px;top:453px;background:var(--red-dark)">Level<br>up</div>
    <div class="power" style="left:105px;top:453px;background:var(--red-soft)">Live+<br>-24</div>
    <div class="power" style="left:168px;top:453px;background:var(--red)">Split<br>-8</div>
    <div class="power" style="left:231px;top:453px;background:var(--red-soft)">Hint<br>-4</div>
    <div class="abs nav-label c" style="left:153px;top:510px">Home</div>
  </div>

  <!-- ================= PAPER MODE ================= -->
  <div class="screen-title" style="left:72px;top:650px">Paper mode</div>
  <div class="screen" style="left:72px;top:680px">
    <div class="status"><span class="abs dots">●●●●● ᯤ</span><span class="abs time c">9:41 AM</span><span class="abs batt">100% <i></i></span></div>
    <div class="abs counter c" style="left:97px;top:42px"><div class="k">WRONG</div><div class="v">0</div></div>
    <div class="abs counter c" style="left:221px;top:42px"><div class="k">CORRECT</div><div class="v">1</div></div>
    <div class="stack" style="left:43px;top:96px;width:220px;height:30px"></div>
    <div class="stack" style="left:30px;top:106px;width:246px;height:30px;background:#d9d9d9"></div>
    <div class="card" style="left:18px;top:115px;width:270px;height:375px"></div>
    <div class="abs" style="left:263px;top:120px;font-size:22px;color:#bbb;font-weight:300">✕</div>
    <div class="abs c jp" style="left:153px;top:138px;font-size:150px;line-height:1;font-weight:500">江</div>
    <div class="band" style="top:362px;height:90px"><div class="jp" style="margin-top:22px;font-size:20px">江</div><div style="font-size:14px;margin-top:2px">Creek</div></div>
    <div class="next" style="top:452px">Next</div>
    <div class="abs nav-label c" style="left:153px;top:510px">Home</div>
  </div>

  <!-- ================= SEARCH ================= -->
  <div class="screen-title" style="left:422px;top:650px">Search</div>
  <div class="screen" style="left:422px;top:680px">
    <div class="status"><span class="abs dots">●●●●● ᯤ</span><span class="abs time c">9:41 AM</span><span class="abs batt">100% <i></i></span></div>
    <div class="abs" style="left:18px;top:30px;font-size:14px;color:var(--muted)">Search</div>
    <svg class="abs" style="left:270px;top:28px" width="20" height="20" viewBox="0 0 20 20"><circle cx="8" cy="8" r="6.5" fill="none" stroke="#222" stroke-width="1.5"/><line x1="13" y1="13" x2="18" y2="18" stroke="#222" stroke-width="1.5"/></svg>
    <div class="abs" style="left:18px;top:58px;width:270px;height:1px;background:var(--line)"></div>
    <div class="abs c" style="left:144px;top:76px;background:var(--red);color:var(--white);font-size:9px;padding:0 12px;height:20px;line-height:20px;border-radius:4px">2278 entries found &nbsp;⌄</div>
    <div class="abs" style="left:269px;top:77px;width:18px;height:18px;border-radius:50%;background:var(--red);color:var(--white);font-size:11px;text-align:center;line-height:18px">?</div>
    <div class="kana" style="top:110px">あ</div><div class="kana" style="top:149px">い</div><div class="kana" style="top:188px">う</div>
    <div class="kana" style="top:226px">え</div><div class="kana" style="top:265px">お</div><div class="kana" style="top:304px">か</div>
    <div class="kana" style="top:342px">が</div><div class="kana" style="top:381px">き</div><div class="kana" style="top:420px">く</div><div class="kana" style="top:458px">け</div>
    <div class="srow" style="top:234px"><span class="abs">e</span><span class="abs" style="left:36px"><i class="mini"></i><i class="mini"></i><i class="mini"></i></span><span class="abs" style="left:98px">Hiragrana</span><span class="abs" style="left:165px">K</span></div>
    <div class="srow" style="top:273px"><span class="abs">o</span><span class="abs" style="left:36px"><i class="mini"></i><i class="mini"></i><i class="mini"></i></span><span class="abs" style="left:98px">Hiragrana</span><span class="abs" style="left:165px">K</span></div>
    <div class="srow" style="top:312px"><span class="abs">ka</span><span class="abs" style="left:36px"><i class="mini"></i><i class="mini"></i><i class="mini"></i></span><span class="abs" style="left:98px">Hiragrana</span><span class="abs" style="left:165px">K</span></div>
    <div class="srow" style="top:350px"><span class="abs">ga</span><span class="abs" style="left:36px"><i class="mini"></i><i class="mini"></i><i class="mini"></i></span><span class="abs" style="left:98px">Hiragrana</span><span class="abs" style="left:165px">K</span></div>
    <div class="srow" style="top:389px"><span class="abs">ki</span><span class="abs" style="left:36px"><i class="mini"></i><i class="mini"></i><i class="mini"></i></span><span class="abs" style="left:98px">Hiragrana</span><span class="abs" style="left:165px">K</span></div>
    <div class="srow" style="top:428px"><span class="abs">ku</span><span class="abs" style="left:36px"><i class="mini"></i><i class="mini"></i><i class="mini"></i></span><span class="abs" style="left:98px">Hiragrana</span><span class="abs" style="left:165px">K</span></div>
    <div class="srow" style="top:466px"><span class="abs">ke</span><span class="abs" style="left:36px"><i class="mini"></i><i class="mini"></i><i class="mini"></i></span><span class="abs" style="left:98px">Hiragrana</span><span class="abs" style="left:165px">K</span></div>
    <div class="star" style="left:272px;top:116px">☆</div><div class="star" style="left:272px;top:155px">☆</div><div class="star" style="left:272px;top:194px">☆</div>
    <div class="star" style="left:272px;top:232px">☆</div><div class="star" style="left:272px;top:271px">☆</div><div class="star" style="left:272px;top:310px">☆</div>
    <div class="star" style="left:272px;top:348px">☆</div><div class="star" style="left:272px;top:387px">☆</div><div class="star" style="left:272px;top:426px">☆</div><div class="star" style="left:272px;top:464px">☆</div>
    <div class="card" style="left:43px;top:96px;width:221px;height:108px;border-radius:4px"></div>
    <div class="abs c" style="left:153px;top:116px;font-size:11px;font-weight:500">Practice Writing</div>
    <div class="abs" style="left:56px;top:145px;font-size:9px">Mark 30848 Tests</div>
    <div class="abs" style="left:156px;top:143px;display:flex;gap:14px"><i class="dot" style="width:13px;height:13px;background:var(--grey)"></i><i class="dot" style="width:13px;height:13px;background:var(--coral)"></i><i class="dot" style="width:13px;height:13px;background:var(--blue)"></i><i class="dot" style="width:13px;height:13px;background:var(--teal)"></i></div>
    <div class="abs" style="left:56px;top:173px;font-size:9px">Mark 2136 Kanjis</div>
    <div class="abs" style="left:202px;top:168px;font-size:20px;line-height:1">☆</div>
    <div class="abs" style="left:230px;top:168px;font-size:20px;line-height:1">★</div>
    <div class="abs" style="left:18px;top:492px;width:270px;height:1px;background:var(--line)"></div>
    <div class="abs nav-label c" style="left:153px;top:510px">Home</div>
  </div>

  <!-- ================= WRITING ================= -->
  <div class="screen-title" style="left:773px;top:650px">Writing</div>
  <div class="screen" style="left:773px;top:680px">
    <div class="status"><span class="abs dots">●●●●● ᯤ</span><span class="abs time c">9:41 AM</span><span class="abs batt">100% <i></i></span></div>
    <div class="abs counter c" style="left:63px;top:42px"><div class="k">REMAINING</div><div class="v">102</div></div>
    <div class="abs counter c" style="left:154px;top:42px"><div class="k">WRONG</div><div class="v">1</div></div>
    <div class="abs counter c" style="left:243px;top:42px"><div class="k">CORRECT</div><div class="v">0</div></div>
    <div class="stack" style="left:43px;top:96px;width:220px;height:30px"></div>
    <div class="stack" style="left:30px;top:106px;width:246px;height:30px;background:#d9d9d9"></div>
    <div class="card" style="left:18px;top:115px;width:270px;height:375px"></div>
    <div class="abs c jp" style="left:153px;top:150px;font-size:150px;line-height:1;font-weight:500">火</div>
    <div class="band" style="top:362px;height:90px">
      <div class="abs c jp" style="left:135px;top:-17px;width:34px;height:34px;border-radius:50%;background:var(--white);color:var(--red);line-height:34px;font-size:15px">火</div>
      <div class="abs" style="right:8px;top:6px;font-size:16px">☆</div>
      <div style="margin-top:26px;font-size:22px;font-weight:300">fire</div>
      <div class="jp" style="font-size:11px;margin-top:4px">カ,ひ</div>
    </div>
    <div class="next" style="top:452px">Next</div>
    <div class="abs nav-label c" style="left:153px;top:508px">Home</div>
  </div>

  <!-- ================= SETTING ================= -->
  <div class="screen-title" style="left:1121px;top:650px">Setting</div>
  <div class="screen" style="left:1121px;top:680px">
    <div class="status"><span class="abs dots">●●●●● ᯤ</span><span class="abs time c">9:41 AM</span><span class="abs batt">100% <i></i></span></div>
    <div class="set-label" style="top:39px">Group Tests by</div>
    <div class="seg" style="top:57px"><span class="on">JLPT Level</span><span>School Year</span></div>
    <div class="set-label" style="top:107px">Size of Answer Grid</div>
    <div class="seg" style="top:125px"><span>3 x 3</span><span class="on">4 x 4</span></div>
    <div class="set-label" style="top:175px">Show Meaning in Tests</div>
    <div class="seg" style="top:193px"><span>Never</span><span class="on">Classic</span><span>Always</span></div>
    <div class="set-label" style="top:244px">Show Pattern in Writing Tests</div>
    <div class="seg" style="top:262px"><span>Never</span><span class="on">Classic</span><span>Always</span></div>
    <div class="set-label" style="top:312px">Tests used in Game</div>
    <div class="seg" style="top:330px"><span>Meaning</span><span>Reading</span><span class="on">Both</span></div>
    <div class="set-label" style="top:381px">Feedback</div>
    <div class="seg" style="top:398px"><span>Rate</span><span style="border-left:1px solid #bbb;border-radius:0;height:20px;margin-top:5px;line-height:20px">Email</span></div>
    <div class="abs" style="left:18px;top:445px;width:270px;height:1px;background:var(--line)"></div>
    <div class="abs c jp" style="left:153px;top:455px;font-size:8.5px">みなさん の べんきょう を こころ から おうえん します</div>
    <div class="abs c" style="left:153px;top:467px;font-size:8.5px;color:#555">many thanks to lexidict.net and strokebase.org</div>
    <div class="abs" style="left:18px;top:492px;width:270px;height:1px;background:var(--line)"></div>
    <div class="abs nav-label c" style="left:153px;top:510px">Home</div>
  </div>

  <!-- ================= FOOTER ================= -->
  <div class="app-mark" role="img" aria-label="Moriva Tutor app icon"></div>
  <div class="brand">Moriva Tutor</div>
  <div class="tagline">UI Design concept</div>
  <p class="about">Moriva Tutor is free. There's no advertising and no in-app purchases are necessary – it's just free, pure and simple.<br>Moriva Tutor knows not only all the 2,136 jōyō kanjis and their readings, but also the 8,000 most common Japanese words and how to<br>pronounce them. This unique combination enables you to learn the Kun- and On-readings of the kanjis and apply and test what you<br>have learnt straight away: both how to read a word and how to write a word you know.</p>

</div>
</div>
</body>
</html>
```